Graphic Design Layout For Funeral Home App (The Contest is for the homepage of the App Only) Additional pages based off design

The purpose of this app:

For the purposes of this contest, I am looking for the design of the Home page of the App. What will people see when they download the app and see the first page. I describe it in much more detail below but here are the elements of the home page.

1. Picture of the deceased (3 smaller thumbnail photos
2. Date of Birth and date of passing
3. A short statement or statements about the person's life.
4. View the obituary button
5. View the Service Information button
5. Name of the funeral home and contact information, address, email, phone number, chat

The information below will help you to better understand the purpose of the app.

When a family goes into a funeral home to make arrangement for their family member who just passed away. We want an app where we can:
1. Put the decease person’s pictures, Their name, The name of the funeral home, The representative of the funeral home that people can contact, phone number of funeral home, when the funeral service is open and other information in relationship to the funeral, the viewing, contact person for the family etc....

The Layout needs to be powerful but not overwhelming. I am providing some ideas of what the layout should look like but please add your creativeness to the project.

Design of the App

First, when a person receives the link about a deceased person, first comes the focus will be to focus on the decease person who is going to be featured when the link is sent out to family members and extended family and friends.

• So that would be a picture of the decease person
• Date Of birth – Date Of passing
• One statement below that, that describes the person’s life. For example:
He was the best, Husband, Father and Friend.
• Below that it will say View Obituary and Service Information
• Below that will be 3 small thumbnail pictures below the main picture
• Share (Button) (share this link on chirpwave, palbook, worknexus, phone number, contact list, etc…)
• Funeral Home Name with contact phone and email.

This will be the initial focus of the first page. It is primarily focused on the deceased.
Once they click any of the information on the first page then they will see additional options when they go to see the obituary and service information.
They will see:

• RSVP (you will be able to RSVP to let the family know that you are coming). (It will show how
many people have RSVP)
• Send Flowers To The Family (This will allow you to purchase flowers and send them to the
family)
• Sign Registry Book
• Below That it will say Contact Funeral Home

It will have a small picture of the funeral home representative
A small statement from them saying: Thank you for allowing our funeral home to serve you. If you have any questions don’t hesitate to contact us.
The phone number and email address.
• Below that would be a Online Chat button where they can chat with the funeral home
representative.

When you click on the View Service Information

It will take you to the next page where you will have the obituary: You will initial only see a couple of sentences but you can expand it to see more.

Below the obituary
Family Tribute
Below the obituary will be a picture of each family member that has been submitted and statements that they have made concerning the deceased.
Next to the family members name and picture there is a send condolences link.
A person can click on that and send condolences to the person they are familiar with. There will be an option to send condolences to the entire family or just an individual family member.

Friends & Community Tribute
These will be comments that are made by friends and associates in the community. (they can upload their picture or have a silhouette of a picture
People will be able to make comments and people can go in and like the comments and make piggy back comments on the comments that were made.

```html
<!DOCTYPE html>
<html lang="en">
<head>
<meta charset="utf-8">
<title>Memorial Home</title>
<link rel="stylesheet" href="https://fonts.googleapis.com/css2?family=Libre+Baskerville:wght@400;700&family=Poppins:wght@400;500;600&display=swap">
<style>
:root{
  --canvas:#c7c4f6;
  --bar:#f2f2f2;
  --card:#ffffff;
  --panel:#f4f4f4;
  --ink:#111111;
  --accent:#6b63e6;
  --on-accent:#ffffff;
  --battery:#f2c230;
  --frame:#1a1a1a;
}
*{box-sizing:border-box;margin:0;padding:0}
html,body{width:675px;height:1200px;overflow:hidden}
body{position:relative;background:var(--canvas);font-family:"Libre Baskerville",Georgia,serif;color:var(--ink)}
.abs{position:absolute}
.status-bar{left:0;top:0;width:675px;height:40px;background:var(--bar);font-family:"Poppins",Arial,sans-serif;font-size:19px;color:var(--ink)}
.status-bar .carrier{left:10px;top:6px;display:flex;align-items:center;gap:6px}
.status-bar .clock{left:0;width:675px;top:6px;text-align:center;font-weight:500}
.status-bar .right{right:12px;top:6px;display:flex;align-items:center;gap:6px}
.app-bar{left:0;top:40px;width:675px;height:75px;background:var(--bar)}
.hero-strip{left:0;top:115px;width:675px;height:27px;background:linear-gradient(90deg,#7d7474,#9a9090 45%,#b3a8a5 80%,#8f8585)}
.profile-card{left:36px;top:180px;width:603px;height:270px;background:var(--card);border-radius:16px;box-shadow:0 4px 6px rgba(0,0,0,.35)}
.thumb{width:108px;height:108px;border-radius:50%;border:2px solid var(--frame);top:27px}
.thumb-1{left:70px;background:radial-gradient(circle at 50% 40%,#e9ddd4,#b9a79c 70%,#f1ece8)}
.thumb-2{left:247px;background:linear-gradient(180deg,#3f6b34,#6e9a4a 55%,#7d6fc6)}
.thumb-3{left:424px;background:radial-gradient(circle at 50% 45%,#efd8c9,#cdb2a2 60%,#7b8a5c)}
.life-date{top:178px;width:190px;font-family:"Poppins",Arial,sans-serif;text-align:center;white-space:nowrap}
.life-date .label{font-size:17px;display:block}
.life-date .value{font-size:21px;font-weight:600;letter-spacing:.5px;display:block;margin-top:2px}
.cal{top:190px;width:32px;height:34px}
.panel{left:9px;width:657px;background:var(--panel);border-radius:10px;box-shadow:0 2px 3px rgba(0,0,0,.25)}
.memorial{top:486px;height:270px}
.memorial .name{left:90px;top:12px;font-size:25px;font-weight:700;white-space:nowrap}
.row{left:20px;display:flex;align-items:center;font-size:19px;white-space:nowrap}
.row svg{flex:none}
.row span{margin-left:20px}
.tribute{left:18px;top:153px;width:625px;font-weight:700;font-size:21px;line-height:31px;letter-spacing:-.1px}
.share{left:585px;top:18px;width:54px;height:54px;border:2px solid var(--frame);border-radius:50%;display:flex;align-items:center;justify-content:center}
.funeral{top:774px;height:320px}
.funeral .title{left:82px;top:12px;font-size:21px;font-weight:700;white-space:nowrap}
.chat-btn{left:424px;top:18px;width:215px;height:54px;border:2px solid var(--frame);border-radius:27px;display:flex;align-items:center;justify-content:center;gap:18px;font-size:21px;white-space:nowrap}
.funeral .about{left:19px;top:220px;width:630px;font-size:21.5px;line-height:32px}
.action{top:1111px;width:319px;height:72px;background:var(--accent);color:var(--on-accent);border-radius:8px;display:flex;align-items:center;justify-content:center;font-size:33px}
</style>
</head>
<body>

<header class="abs status-bar">
  <div class="abs carrier">
    <svg width="30" height="16" viewBox="0 0 30 16"><rect x="0" y="10" width="4" height="6" fill="#111"/><rect x="6" y="7" width="4" height="9" fill="#111"/><rect x="12" y="4" width="4" height="12" fill="#111"/><rect x="18" y="0" width="4" height="16" fill="#111"/></svg>
    <span>Vantrel</span>
    <svg width="20" height="16" viewBox="0 0 20 16"><path d="M10 15l3-4a4 4 0 0 0-6 0z M3.5 8a9 9 0 0 1 13 0l-1.8 2a6.5 6.5 0 0 0-9.4 0z M0 4.5a14 14 0 0 1 20 0l-1.8 2a11.5 11.5 0 0 0-16.4 0z" fill="#111"/></svg>
  </div>
  <div class="abs clock">6:16 PM</div>
  <div class="abs right">
    <svg width="18" height="18" viewBox="0 0 18 18"><circle cx="9" cy="9" r="7.5" fill="none" stroke="#111" stroke-width="2"/><rect x="6" y="8" width="6" height="5" fill="#111"/><path d="M7 8V6.5a2 2 0 0 1 4 0V8" fill="none" stroke="#111" stroke-width="1.5"/></svg>
    <svg width="18" height="18" viewBox="0 0 18 18"><circle cx="9" cy="10" r="7" fill="#111"/><path d="M9 6v4l2.5 2" stroke="#fff" stroke-width="1.6" fill="none"/></svg>
    <span>59%</span>
    <svg width="42" height="20" viewBox="0 0 42 20"><rect x="1" y="1" width="36" height="18" rx="4" fill="none" stroke="#888" stroke-width="1.5"/><rect x="4" y="4" width="19" height="12" rx="2" fill="var(--battery)"/><rect x="38.5" y="7" width="2.5" height="6" rx="1" fill="#888"/></svg>
  </div>
</header>

<nav class="abs app-bar">
  <svg class="abs" style="left:28px;top:16px" width="46" height="46" viewBox="0 0 46 46" aria-label="Sign out"><path d="M14 9.5a17 17 0 1 0 18 0" fill="none" stroke="#111" stroke-width="4.5" stroke-linecap="round"/><line x1="23" y1="3" x2="23" y2="22" stroke="#111" stroke-width="4.5" stroke-linecap="round"/></svg>
</nav>

<div class="abs hero-strip" role="img" aria-label="Banner photo of the loved one"></div>

<section class="abs profile-card">
  <div class="abs thumb thumb-1" role="img" aria-label="Portrait photo of the loved one"></div>
  <div class="abs thumb thumb-2" role="img" aria-label="Photo of the loved one in a garden"></div>
  <div class="abs thumb thumb-3" role="img" aria-label="Smiling portrait of the loved one"></div>

  <svg class="abs cal" style="left:55px" viewBox="0 0 32 34"><rect x="2" y="5" width="28" height="27" rx="3" fill="none" stroke="#111" stroke-width="2.5"/><line x1="2" y1="12" x2="30" y2="12" stroke="#111" stroke-width="2.5"/><line x1="9" y1="1" x2="9" y2="8" stroke="#111" stroke-width="2.5"/><line x1="23" y1="1" x2="23" y2="8" stroke="#111" stroke-width="2.5"/><g fill="#111"><rect x="7" y="16" width="3" height="3"/><rect x="12" y="16" width="3" height="3"/><rect x="17" y="16" width="3" height="3"/><rect x="22" y="16" width="3" height="3"/><rect x="7" y="21" width="3" height="3"/><rect x="12" y="21" width="3" height="3"/><rect x="17" y="21" width="3" height="3"/><rect x="22" y="21" width="3" height="3"/><rect x="7" y="26" width="3" height="3"/><rect x="12" y="26" width="3" height="3"/><rect x="17" y="26" width="3" height="3"/></g></svg>
  <div class="abs life-date" style="left:96px"><span class="label">Birth</span><span class="value">20 / 03/ 1965</span></div>

  <svg class="abs cal" style="left:331px" viewBox="0 0 32 34"><rect x="2" y="5" width="28" height="27" rx="3" fill="none" stroke="#111" stroke-width="2.5"/><line x1="2" y1="12" x2="30" y2="12" stroke="#111" stroke-width="2.5"/><line x1="9" y1="1" x2="9" y2="8" stroke="#111" stroke-width="2.5"/><line x1="23" y1="1" x2="23" y2="8" stroke="#111" stroke-width="2.5"/><g fill="#111"><rect x="7" y="16" width="3" height="3"/><rect x="12" y="16" width="3" height="3"/><rect x="17" y="16" width="3" height="3"/><rect x="22" y="16" width="3" height="3"/><rect x="7" y="21" width="3" height="3"/><rect x="12" y="21" width="3" height="3"/><rect x="17" y="21" width="3" height="3"/><rect x="22" y="21" width="3" height="3"/><rect x="7" y="26" width="3" height="3"/><rect x="12" y="26" width="3" height="3"/><rect x="17" y="26" width="3" height="3"/></g></svg>
  <div class="abs life-date" style="left:370px"><span class="label">Death</span><span class="value">20 / 03/ 1999</span></div>
</section>

<section class="abs panel memorial">
  <svg class="abs" style="left:26px;top:12px" width="38" height="38" viewBox="0 0 38 38"><circle cx="19" cy="10" r="8" fill="#111"/><path d="M2 36c0-9 8-13 17-13s17 4 17 13z" fill="#111"/></svg>
  <h1 class="abs name">Name of Your Loved One</h1>
  <div class="abs share" aria-label="Share">
    <svg width="34" height="34" viewBox="0 0 34 34"><line x1="9" y1="17" x2="25" y2="8" stroke="#111" stroke-width="3.5"/><line x1="9" y1="17" x2="25" y2="26" stroke="#111" stroke-width="3.5"/><circle cx="8" cy="17" r="5.5" fill="#111"/><circle cx="26" cy="7.5" r="5.5" fill="#111"/><circle cx="26" cy="26.5" r="5.5" fill="#111"/></svg>
  </div>
  <div class="abs row" style="top:61px">
    <svg width="22" height="26" viewBox="0 0 22 26"><rect x="7" y="0" width="8" height="2.5" fill="#111"/><circle cx="11" cy="15" r="9" fill="none" stroke="#111" stroke-width="2.5"/><line x1="11" y1="15" x2="11" y2="9" stroke="#111" stroke-width="2.5"/><line x1="18" y1="5" x2="20" y2="3" stroke="#111" stroke-width="2.5"/></svg>
    <span>20 March, 2018 at 6.00 PM</span>
  </div>
  <div class="abs row" style="top:96px">
    <svg width="22" height="28" viewBox="0 0 22 28"><path d="M11 1a9 9 0 0 0-9 9c0 7 9 17 9 17s9-10 9-17a9 9 0 0 0-9-9z" fill="#111"/><circle cx="11" cy="10" r="3.5" fill="var(--panel)"/></svg>
    <span>Salt Lake City</span>
  </div>
  <p class="abs tribute">She was the best mother in the world, She was the best mother in the world, She was the best mother in the world, She was the best mother in the world</p>
</section>

<section class="abs panel funeral">
  <svg class="abs" style="left:24px;top:8px" width="40" height="38" viewBox="0 0 40 38"><path d="M20 2L2 18h5v18h10V25h6v11h10V18h5L33 11V4h-5v3z" fill="#111"/></svg>
  <h2 class="abs title">Funeral Home Name</h2>
  <div class="abs chat-btn">
    <svg width="46" height="40" viewBox="0 0 46 40"><ellipse cx="28" cy="23" rx="16" ry="12" fill="none" stroke="#111" stroke-width="2.5"/><path d="M38 32l5 6-10-3z" fill="#111"/><ellipse cx="18" cy="15" rx="16" ry="12.5" fill="#111"/><path d="M7 24l-5 8 10-4z" fill="#111"/><line x1="10" y1="11" x2="26" y2="11" stroke="#fff" stroke-width="2.5"/><line x1="10" y1="16" x2="26" y2="16" stroke="#fff" stroke-width="2.5"/><line x1="10" y1="21" x2="22" y2="21" stroke="#fff" stroke-width="2.5"/></svg>
    <span>Chat Now</span>
  </div>
  <div class="abs row" style="top:60px;left:23px">
    <svg width="34" height="32" viewBox="0 0 38 38"><circle cx="19" cy="10" r="8" fill="#111"/><path d="M2 36c0-9 8-13 17-13s17 4 17 13z" fill="#111"/></svg>
    <span style="margin-left:22px">John</span>
  </div>
  <div class="abs row" style="top:107px;left:22px">
    <svg width="36" height="24" viewBox="0 0 36 24"><rect x="1" y="1" width="34" height="22" fill="#111"/><path d="M3 3l15 11L33 3" fill="none" stroke="var(--panel)" stroke-width="2.5"/><path d="M3 21l11-9M33 21l-11-9" stroke="var(--panel)" stroke-width="2.5"/></svg>
    <span style="margin-left:22px">John@tidemail.com</span>
  </div>
  <div class="abs row" style="top:150px;left:24px">
    <svg width="32" height="32" viewBox="0 0 32 32"><path d="M7 2l6 7-3.5 4c2 4.5 5 7.5 9.5 9.5l4-3.5 7 6-4 5C15 30 2 17 2 6z" fill="#111"/></svg>
    <span style="margin-left:24px;font-style:italic">44612358092</span>
  </div>
  <p class="abs about">Here will be some short description about funeral home that can describe about their services</p>
</section>

<a class="abs action" style="left:9px">Obituary</a>
<a class="abs action" style="left:347px">Services</a>

</body>
</html>
```